Etiketten-Design für familiengeführten Weinbaubetrieb
Zielgruppe
Wir sind ein Familiengeführter Weinbaubetrieb und vermarkten unseren Wein in 0,75l Flaschen sowie auch Säfte und Schnäpse.
Zur zeit Verkaufen wir unseren Wein an Gastro und Private Kunden auch teils über Messen
Aufgabenstellung
Das derzeitige Etikett ist recht schlicht gestaltet und das Logo besteht rein aus dem geschriebenen Namen Winzerhof Dolmeck. Es kann aber auch gerne nur mit dem Namen Dolmeck ohne Winzerhof gearbeitet werden! Mit dem einbringen einer neuen Generation in den Betrieb wollen wir das aussehen unserer Produkte erneuern. Dazu kann sich gerne mit dem Namen als 'Logo' in jeglicher Art gespielt werden. Wir füllen unsere Weine in 0,75l Bordeaux Flaschen. Die Form des Etikett ist kein K.O. Kriterium jedoch wurde ursprünglich ein rund um Etikett angedacht. Sollten die Designes sich auch anders realisieren lassen sind wir gerne offen für Ideen.

```html
<!DOCTYPE html>
<html lang="de">
<head>
<meta charset="utf-8">
<title>Dolmeck – Etikettenserie 2023</title>
<link rel="stylesheet" href="https://fonts.googleapis.com/css2?family=Playfair+Display:wght@700&family=Roboto+Slab:wght@400&family=Josefin+Sans:wght@400&display=swap">
<style>
  :root {
    --page: #ffffff;
    --ink: #ffffff;
    --feder: #b6c23a;
    --feder-edge: #9aa434;
    --riesling: #c2b058;
    --riesling-edge: #ab9b50;
    --blau: #533f4c;
    --blau-edge: #3d2f39;
    --riserva: #4f2124;
    --riserva-edge: #3a191b;
  }
  * { margin: 0; padding: 0; box-sizing: border-box; }
  html, body {
    width: 1200px; height: 1200px; overflow: hidden;
    background: var(--page);
  }
  .label-series {
    position: relative; width: 1200px; height: 1200px;
  }
  .label {
    position: absolute; top: 646px;
    width: 202px; height: 166px;
    color: var(--ink);
    text-align: center;
    overflow: hidden;
  }
  .label--feder    { left: 108px; background: linear-gradient(90deg, var(--feder-edge) 0 8%, var(--feder) 8% 92%, var(--feder-edge) 92%); }
  .label--riesling { left: 374px; background: linear-gradient(90deg, var(--riesling-edge) 0 8%, var(--riesling) 8% 92%, var(--riesling-edge) 92%); }
  .label--blau     { left: 642px; background: linear-gradient(90deg, var(--blau-edge) 0 8%, var(--blau) 8% 92%, var(--blau-edge) 92%); }
  .label--riserva  { left: 905px; background: linear-gradient(90deg, var(--riserva-edge) 0 8%, var(--riserva) 8% 92%, var(--riserva-edge) 92%); }

  .label__brush {
    position: absolute; left: 36px; top: 10px;
    width: 130px; height: 150px;
    border-radius: 50% 50% 40% 40%;
    background: radial-gradient(ellipse at center, rgba(0,0,0,0.10), rgba(0,0,0,0) 70%);
  }
  .label__mark {
    position: absolute; left: 50%; top: 13px;
    width: 22px; height: 22px; margin-left: -11px;
    border: 1px solid var(--ink); border-radius: 50%;
  }
  .label__brand {
    position: absolute; left: 0; right: 0; top: 40px;
    font: 700 9.5px/1 "Playfair Display", serif;
    letter-spacing: 1.6px;
  }
  .label__name {
    position: absolute; left: 0; right: 0; top: 58px; height: 62px;
    display: flex; flex-direction: column; justify-content: center;
    font: 400 24px/1.05 "Roboto Slab", serif;
    letter-spacing: 2px;
  }
  .label--blau .label__name { letter-spacing: 1px; }
  .label__year {
    position: absolute; left: 0; right: 0; top: 137px;
    font: 400 8.5px/1 "Josefin Sans", sans-serif;
    letter-spacing: 2px;
  }
</style>
</head>
<body>
<main class="label-series">
  <section class="label label--feder">
    <div class="label__brush" role="img" aria-label="Pinselstrich-Weinrebe als Hintergrundmotiv"></div>
    <span class="label__mark"></span>
    <p class="label__brand">DOLMECK</p>
    <h2 class="label__name"><span>FEDER</span><span>WEISER</span></h2>
    <p class="label__year">2023</p>
  </section>
  <section class="label label--riesling">
    <div class="label__brush" role="img" aria-label="Pinselstrich-Weinrebe als Hintergrundmotiv"></div>
    <span class="label__mark"></span>
    <p class="label__brand">DOLMECK</p>
    <h2 class="label__name"><span>RIESLING</span></h2>
    <p class="label__year">2023</p>
  </section>
  <section class="label label--blau">
    <div class="label__brush" role="img" aria-label="Pinselstrich-Weinrebe als Hintergrundmotiv"></div>
    <span class="label__mark"></span>
    <p class="label__brand">DOLMECK</p>
    <h2 class="label__name"><span>BLAU</span><span>BURGUNDER</span></h2>
    <p class="label__year">2023</p>
  </section>
  <section class="label label--riserva">
    <div class="label__brush" role="img" aria-label="Pinselstrich-Weinrebe als Hintergrundmotiv"></div>
    <span class="label__mark"></span>
    <p class="label__brand">DOLMECK</p>
    <h2 class="label__name"><span>RISERVA</span></h2>
    <p class="label__year">2023</p>
  </section>
</main>
</body>
</html>
```